Professional, modern and unique business card. We are looking to present a new look to our business cards however we don't want to divert too far away from original template. We want social media links and our 3 office addresses on the backside of the business cards. Please see attached business card templates for ideas.
Cobalt Homes Color Code:
R: 7
G:63
B:86

Target Market(s)

Real Estate

Industry/Entity Type

Real Estate

Contact Information for Business Card

Follow the attached templates. In need of a more modern and unique touch but don't want to divert from the original theme or color.
Cobalt Homes Color Code:
R: 7
G:63
B:86

Font styles to use
Serif

Requirements
Must have
• Cobalt Homes logo, Cobalt homes colors, social media links, 3 office addresses,
Nice to have
• information about Cobalt Homes and QR codes. You can check out www.mycobalthomesagent.com

```html
<!DOCTYPE html>
<html lang="en">
<head>
<meta charset="utf-8">
<title>Cobalt Homes Business Card</title>
<link href="https://fonts.googleapis.com/css2?family=Marcellus&family=Lato:wght@400;700&display=swap" rel="stylesheet">
<style>
:root{
  --backdrop:#3b3532;
  --card:#0f1011;
  --card-edge:#1c1d1f;
  --ice:#c4d6df;
  --silver:#d7dde0;
  --muted:#9aa6ac;
  --rule:#2e3336;
  --cobalt:rgb(7,63,86);
  --dot:#5b7f8f;
}
*{margin:0;padding:0;box-sizing:border-box}
html,body{width:1200px;height:844px;overflow:hidden;background:var(--backdrop)}
.stage{position:relative;width:1200px;height:844px}
.card{position:absolute;top:268px;width:540px;height:309px;background:var(--card);border:1px solid var(--card-edge);box-shadow:0 10px 30px rgba(0,0,0,.45);font-family:'Lato',sans-serif;color:var(--silver);overflow:hidden}
.card--front{left:40px}
.card--back{left:620px}

.brand{display:flex;align-items:center;gap:9px;font-family:'Marcellus',serif;color:var(--ice);letter-spacing:.06em;white-space:nowrap}
.brand__dot{width:14px;height:14px;border-radius:50%;background:var(--cobalt);border:1px solid var(--dot);flex:none}

.card--front .brand{position:absolute;left:30px;top:170px;font-size:23px}
.front__divider{position:absolute;left:276px;top:60px;width:1px;height:190px;background:var(--rule)}
.person{position:absolute;left:298px;top:80px}
.person__name{font-family:'Marcellus',serif;font-size:21px;font-weight:400;color:var(--ice);letter-spacing:.04em}
.person__title{font-size:11.5px;letter-spacing:.12em;color:var(--muted);margin-top:2px}
.contact{list-style:none;margin-top:14px}
.contact li{display:flex;align-items:center;gap:9px;font-size:13px;line-height:19px;color:var(--silver);white-space:nowrap}
.contact svg{width:11px;height:11px;fill:var(--silver);flex:none}

.card--back .brand{position:absolute;left:0;right:0;top:42px;justify-content:center;font-size:28px}
.socials{position:absolute;left:34px;right:34px;top:120px;display:grid;grid-template-columns:repeat(3,auto);gap:12px 18px;justify-content:center}
.social{display:flex;align-items:center;gap:7px;font-size:12.5px;color:var(--silver);white-space:nowrap}
.social__dot{width:14px;height:14px;border-radius:50%;background:var(--dot);flex:none}
.back__divider{position:absolute;left:34px;right:34px;top:196px;height:1px;background:var(--rule)}
.offices{position:absolute;left:34px;right:34px;top:214px;display:flex;justify-content:space-between}
.office{font-size:12.5px;line-height:18px;color:var(--silver)}
</style>
</head>
<body>
<main class="stage">
  <section class="card card--front">
    <div class="brand"><span class="brand__dot"></span>COBALT HOMES</div>
    <div class="front__divider"></div>
    <div class="person">
      <h1 class="person__name">DANA WHITFIELD</h1>
      <p class="person__title">MANAGING DIRECTOR</p>
      <ul class="contact">
        <li><svg viewBox="0 0 12 12"><path d="M2 1h2.5l1 3-1.5 1a7 7 0 0 0 3 3l1-1.5 3 1V11C5.5 11 1 6.5 1 2z"/></svg>212 730 4418</li>
        <li><svg viewBox="0 0 12 12"><path d="M3 0h6v12H3zM4 1.5v8h4v-8z"/></svg>917 264 0391</li>
        <li><svg viewBox="0 0 12 12"><path d="M3 0h6v3H3zM1 4h10v5H9v3H3V9H1zM4 8v3h4V8z"/></svg>212 730 4420</li>
        <li><svg viewBox="0 0 12 12"><path d="M0 2h12v8H0zM1 3l5 3.5L11 3v-.2H1z"/></svg>info@cobalthomesmail.com</li>
        <li><svg viewBox="0 0 12 12"><path d="M6 0a6 6 0 1 0 0 12A6 6 0 0 0 6 0zm0 1.5c.6.8 1 2.3 1.1 3.8H4.9C5 3.8 5.4 2.3 6 1.5zM4.9 6.7h2.2c-.1 1.5-.5 3-1.1 3.8-.6-.8-1-2.3-1.1-3.8z"/></svg>www.mycobalthomesagent.com</li>
      </ul>
    </div>
  </section>

  <section class="card card--back">
    <div class="brand"><span class="brand__dot"></span>COBALT HOMES</div>
    <div class="socials">
      <span class="social"><span class="social__dot"></span>CobalthomesNY</span>
      <span class="social"><span class="social__dot"></span>Info at Cobalt Homes</span>
      <span class="social"><span class="social__dot"></span>@CobaltHomesNY</span>
      <span class="social"><span class="social__dot"></span>Cobalt Homes</span>
      <span class="social"><span class="social__dot"></span>Cobalt Homes New York</span>
      <span class="social"><span class="social__dot"></span>@CobaltHomesQ</span>
    </div>
    <div class="back__divider"></div>
    <div class="offices">
      <p class="office">418-20 Harbor Blvd<br>Bayview, NY 11370</p>
      <p class="office">62-40 Maple Blvd<br>Elm Park, NY 11428</p>
      <p class="office">1750 Orchard Ave<br>Westbrook, NY 11236</p>
    </div>
  </section>
</main>
</body>
</html>
```